Professional business cards for real estate development company

I need business cards for my new real estate development company. The company, "LUMAR" is a real estate development, investment, and advisory firm with a focus on multifamily, office, and mixed-use projects across primary and secondary markets in the Southeast United States.

Style preference is modern

Industry/Entity Type

Real Estate Development

Contact Information for Business Card

The business cards need to include:
Name
Title
Mailing Address
Phone Number
Web Address

Logo is attached. I would like white to be the primary color with incorporation of the company colors: #232D3A and #B5A451

Font styles to use
Other font styles liked:
• Montserrat, Avenir

Requirements
Must have
• Company Logo. No need to include the company name since the name is in the logo.
Should not have
• No line type designs

```html
<!DOCTYPE html>
<html lang="en">
<head>
<meta charset="utf-8">
<title>LUMAR Business Cards</title>
<link href="https://fonts.googleapis.com/css2?family=Montserrat:wght@400;500;700&display=swap" rel="stylesheet">
<style>
  :root {
    --navy: #232D3A;
    --gold: #B5A451;
    --white: #FFFFFF;
    --paper: #F7F7F5;
    --stage: #E9E9E7;
    --ink: #232D3A;
  }
  * { margin: 0; padding: 0; box-sizing: border-box; }
  html, body {
    width: 1200px;
    height: 900px;
    overflow: hidden;
    background: var(--stage);
    font-family: "Montserrat", sans-serif;
  }
  .canvas {
    position: relative;
    width: 1200px;
    height: 900px;
  }
  .card {
    position: absolute;
    left: 268px;
    width: 665px;
    height: 380px;
    box-shadow: 0 10px 30px rgba(0,0,0,0.12);
    overflow: hidden;
  }
  .card--back { top: 50px; background: var(--navy); }
  .card--front { top: 470px; background: var(--paper); }

  .accent-bar {
    position: absolute;
    right: 0;
    width: 26px;
    height: 96px;
    background: var(--gold);
  }
  .card--back .accent-bar { top: 236px; }
  .card--front .accent-bar { top: 196px; }

  .wordmark {
    position: absolute;
    display: flex;
    align-items: center;
    gap: 14px;
    font-weight: 500;
    font-size: 44px;
    letter-spacing: 6px;
    line-height: 1;
  }
  .wordmark__square {
    width: 18px;
    height: 18px;
  }
  .card--back .wordmark { right: 80px; top: 222px; color: var(--white); }
  .card--back .wordmark__square { background: var(--white); }
  .card--front .wordmark { right: 92px; top: 172px; color: var(--navy); }
  .card--front .wordmark__square { background: var(--navy); }

  .holder {
    position: absolute;
    left: 52px;
    top: 50px;
  }
  .holder__name {
    font-weight: 700;
    font-size: 20px;
    color: var(--gold);
  }
  .holder__title {
    font-weight: 500;
    font-size: 14px;
    color: var(--ink);
    margin-top: 3px;
  }
  .address {
    position: absolute;
    left: 52px;
    top: 160px;
    font-style: normal;
    font-size: 14px;
    line-height: 20px;
    color: var(--ink);
    font-weight: 500;
  }
  .contacts {
    position: absolute;
    left: 32px;
    top: 222px;
    list-style: none;
    font-size: 14px;
    line-height: 22px;
    color: var(--ink);
    font-weight: 500;
  }
  .contacts li {
    display: flex;
    align-items: center;
    gap: 8px;
  }
  .contacts svg {
    width: 12px;
    height: 12px;
    fill: var(--gold);
    flex: none;
  }
  .contacts .contacts__plain { padding-left: 20px; }
</style>
</head>
<body>
<main class="canvas">
  <section class="card card--back" aria-label="Card back">
    <div class="wordmark"><span class="wordmark__square"></span>LUMAR</div>
    <div class="accent-bar"></div>
  </section>

  <section class="card card--front" aria-label="Card front">
    <div class="holder">
      <p class="holder__name">Daniel Harwick</p>
      <p class="holder__title">managing director</p>
    </div>
    <address class="address">
      1450 Crestview Lane NE<br>
      Atlanta, GA 30309
    </address>
    <ul class="contacts">
      <li>
        <svg viewBox="0 0 24 24" aria-hidden="true"><path d="M6.6 10.8a15.1 15.1 0 0 0 6.6 6.6l2.2-2.2a1 1 0 0 1 1-.25 11.4 11.4 0 0 0 3.6.57 1 1 0 0 1 1 1V20a1 1 0 0 1-1 1A17 17 0 0 1 3 4a1 1 0 0 1 1-1h3.5a1 1 0 0 1 1 1c0 1.25.2 2.45.57 3.57a1 1 0 0 1-.25 1z"/></svg>
        404 555 0182
      </li>
      <li>
        <svg viewBox="0 0 24 24" aria-hidden="true"><path d="M2 5h20v3l-10 6L2 8z"/><path d="M2 10l10 6 10-6v9H2z"/></svg>
        info@lumardevelopment.com
      </li>
      <li>
        <svg viewBox="0 0 24 24" aria-hidden="true"><path d="M12 2a10 10 0 1 0 0 20 10 10 0 0 0 0-20zm6.9 6h-3a15.6 15.6 0 0 0-1.4-3.6A8 8 0 0 1 18.9 8zM12 4c.8 1.2 1.5 2.5 1.9 4h-3.8c.4-1.5 1.1-2.8 1.9-4zM4.3 14a8 8 0 0 1 0-4h3.4a16 16 0 0 0 0 4zm.8 2h3a15.6 15.6 0 0 0 1.4 3.6A8 8 0 0 1 5.1 16zm3-8h-3a8 8 0 0 1 4.4-3.6A15.6 15.6 0 0 0 8.1 8zM12 20c-.8-1.2-1.5-2.5-1.9-4h3.8c-.4 1.5-1.1 2.8-1.9 4zm2.3-6H9.7a14.7 14.7 0 0 1 0-4h4.6a14.7 14.7 0 0 1 0 4zm.2 5.6a15.6 15.6 0 0 0 1.4-3.6h3a8 8 0 0 1-4.4 3.6zm1.8-5.6a16 16 0 0 0 0-4h3.4a8 8 0 0 1 0 4z"/></svg>
        www.lumardevelopment.com
      </li>
      <li class="contacts__plain">www.lumardevelopment.com</li>
    </ul>
    <div class="wordmark"><span class="wordmark__square"></span>LUMAR</div>
    <div class="accent-bar"></div>
  </section>
</main>
</body>
</html>
```